BRAMLEIGH real estate family office

Hello, Our business is a real estate intermediation activity on high-end goods (amounts exceeding € 10m) for corporate and private clients. You can see our logo on the site www.bramleigh-invented.fr We would like to keep that spirit with the hexagon that represents France (transactions between Monaco and Saint Tropez, Courchevel and Paris). And the "baseline" that is "real estate family office". The corporate logo should be and can be printed by embossing (relief). We must integrate the name, first name, phone, email and website. Finally, to imbibe the spirit of business, here is a detail of the activity. "Genuine consulting firm in real estate investments, BRAMLEIGH works with its customers as a specialized player in the high-end markets, we are recognized for our ultra-confidential approach and tailor-made, as well as the quality of our network. We broadcast any information on the market and we work exclusively through a strong relationship we have developed over the years. BRAMLEIGH is active on the French Riviera (from Monaco to Saint-Tropez), the Alps (Courchevel, Méribel, Megève) and Paris (essentially market premium). Always looking for opportunities for our clients, we work on two investment areas: residential luxury real estate (properties, vineyards, mansions, land, etc.) commercial real estate (empty office buildings or yield, hotel properties, land, etc.) "

Target Market(s)

High foreign end customers. corporate and private.

Industry/Entity Type

Real Estate

Contact Information for Business Card

LOGO
baseline
Laurent Dufossé
+33(0)6.41.57.09.64
ld@bramleigh-invented.fr
www.bramleigh-invented.fr

Font styles to use
Serif

Colors
cedeed
0255a3
3277b5
85abd2
85cae6
34a7d7
0792cd
cfdeed
1b1b1b

Requirements
Must have
• see description

```html
<!DOCTYPE html>
<html lang="fr">
<head>
<meta charset="utf-8">
<title>BRAMLEIGH — business card</title>
<link href="https://fonts.googleapis.com/css2?family=Questrial&family=Lato:wght@700&display=swap" rel="stylesheet">
<style>
  :root {
    --backdrop: #e4e4e4;
    --card-white: #f7f7f7;
    --card-grey: #ececec;
    --navy: #212a78;
    --navy-deep: #1d2468;
    --azure: #1c8fd6;
    --ink: #4a4a4a;
    --ink-soft: #5a5a5a;
  }
  html, body {
    margin: 0;
    padding: 0;
    overflow: hidden;
  }
  body {
    width: 1200px;
    height: 443px;
    background: var(--backdrop);
    position: relative;
    font-family: "Questrial", "Century Gothic", sans-serif;
  }
  .card {
    position: absolute;
    box-shadow: 2px 3px 6px rgba(0, 0, 0, 0.28);
    overflow: hidden;
  }
  .card--front {
    left: 81px;
    top: 72px;
    width: 486px;
    height: 294px;
    background: linear-gradient(180deg, var(--card-white) 0%, var(--card-grey) 100%);
  }
  .card--back {
    left: 602px;
    top: 71px;
    width: 481px;
    height: 291px;
    background: linear-gradient(160deg, var(--navy) 0%, var(--navy-deep) 100%);
  }
  .brand {
    position: absolute;
    left: 35px;
    top: 44px;
  }
  .brand__name {
    display: block;
    font-size: 38px;
    letter-spacing: 2px;
    color: var(--ink);
    line-height: 1;
  }
  .brand__baseline {
    display: block;
    text-align: right;
    font-size: 11px;
    letter-spacing: 0.6px;
    color: var(--navy);
    margin-top: 3px;
  }
  .contact {
    position: absolute;
    left: 255px;
    top: 156px;
  }
  .contact__name {
    font-family: "Lato", "Calibri", sans-serif;
    font-weight: 700;
    font-size: 18px;
    color: var(--ink-soft);
    margin: 0 0 6px;
  }
  .contact__list {
    list-style: none;
    margin: 0;
    padding: 0;
  }
  .contact__item {
    display: flex;
    align-items: center;
    height: 18px;
    font-size: 15px;
    color: var(--ink-soft);
  }
  .contact__icon {
    width: 10px;
    height: 10px;
    margin: 0 13px 0 3px;
    fill: var(--navy);
  }
  .front-band {
    position: absolute;
    left: 0;
    bottom: 0;
    width: 486px;
    height: 14px;
  }
  .back-mark {
    position: absolute;
    left: 0;
    right: 0;
    top: 127px;
    text-align: center;
    font-size: 34px;
    letter-spacing: 3px;
    color: var(--azure);
    line-height: 1;
  }
</style>
</head>
<body>

<section class="card card--front" aria-label="Card front">
  <div class="brand">
    <span class="brand__name">BRAMLEIGH</span>
    <span class="brand__baseline">real estate family office</span>
  </div>

  <div class="contact">
    <p class="contact__name">Laurent Dufossé</p>
    <ul class="contact__list">
      <li class="contact__item">
        <svg class="contact__icon" viewBox="0 0 10 10" aria-hidden="true">
          <path d="M1 3.2c0-1.2 1.8-2 4-2s4 .8 4 2v.8H7V3H3v1H1z M2.2 5 3.5 4h3l1.3 1v3.8H2.2z"/>
        </svg>
        +33(0)6.41.57.09.64
      </li>
      <li class="contact__item">
        <svg class="contact__icon" viewBox="0 0 10 10" aria-hidden="true">
          <path d="M0.5 2h9v6h-9z M1 2.5 5 5.6 9 2.5" stroke="#f3f3f3" stroke-width="0.7"/>
        </svg>
        ld@bramleigh-invented.fr
      </li>
      <li class="contact__item">
        <svg class="contact__icon" viewBox="0 0 10 10" aria-hidden="true">
          <circle cx="5" cy="5" r="4.3"/>
          <path d="M0.7 5h8.6 M5 0.7v8.6 M1.5 3h7 M1.5 7h7" stroke="#f3f3f3" stroke-width="0.6" fill="none"/>
          <ellipse cx="5" cy="5" rx="2" ry="4.3" stroke="#f3f3f3" stroke-width="0.6" fill="none"/>
        </svg>
        www.bramleigh-invented.fr
      </li>
    </ul>
  </div>

  <svg class="front-band" viewBox="0 0 486 14" aria-hidden="true">
    <polygon points="0,0 340,0 317,14 0,14" fill="var(--navy)"/>
    <polygon points="346,0 486,0 486,14 323,14" fill="var(--azure)"/>
    <polygon points="340,0 346,0 323,14 317,14" fill="#ffffff"/>
  </svg>
</section>

<section class="card card--back" aria-label="Card back">
  <div class="back-mark">BRAMLEIGH</div>
</section>

</body>
</html>
```